Lone Star Wetland Flora Stewardship Guild

We need to design the home page of this new website. We would like a fun website design for provides as a resource for members and information for potential members.
Please design so that we can see a portion of background on each side on the website.
I just need the final design files psd no coding needed.
Attached is their logo (colors are not 100% set in stone either so can mess with those as I did in the quick mockup attached)
Attached is a pdf newsletter they send out, you can get a feel for them and what they are about. The design is crappy and we are here to fix that going forward and we are starting with the website.
Here are some quick example websites (design style is open)
- I attached a quick mockup i did just for a content visual but by all means do what you want.
- http://www.brindlecourtleaders.org/
- http://www.qvelto.org/
- http://preview.plimworks7.com/view.php?cat=layoutpacks&host=gridcrafthub&temp=venrolite
- http://www.ploughvale.org/
- http://www.townmarrow.org/
- http://www.projectkindlecoat.org/
here are some of the other chapters website (pretty bad!)
and here are some of the others:
- http://www.zrelkq.org/
- http://ovtu.org/
- http://www.lirvx.org/
Content Items that need to be included:
1. Logo
2. Menu - home, about, members, resources, events, membership, contact
3. Become a member - button or action
4. social links - friendwall, jobrungo, clipzora
5. banner - that needs to explain their purpose "Promoting environmental stewardship through operations, research, education and outreach" (or this can be worked into the design)
6. Upcoming event (s)
7. Advertisement - members can place an ad on the website, this can be a placeholder for now
8. newsletter signup
9. advertise with us - this link can be in the footer
30-60 years of age, succesfull (household budgets of 120K+ men and women that live in texas.
Education

```html
<!DOCTYPE html>
<html lang="en">
<head>
<meta charset="utf-8">
<title>Lone Star Wetland Flora Stewardship Guild</title>
<link href="https://fonts.googleapis.com/css2?family=Open+Sans:wght@300;400;600;700;800&display=swap" rel="stylesheet">
<style>
:root{
  --crimson:#9a1d3f;
  --crimson-dark:#7e1633;
  --yellow:#f4d60c;
  --gold:#cdb20a;
  --navy:#1c2859;
  --ink:#333333;
  --charcoal:#2f2f2f;
  --graphite:#3d3d3d;
  --night:#1f1f1f;
  --paper:#f1f1f1;
  --white:#ffffff;
  --muted:#a9a9a9;
}
*{box-sizing:border-box;margin:0;padding:0}
html,body{width:720px;height:1200px;overflow:hidden}
body{font-family:"Open Sans",Arial,sans-serif;background:var(--paper);color:var(--ink);position:relative}
section,header,nav,footer{position:absolute;left:0;width:720px}

.topbar{top:0;height:44px;background:linear-gradient(#474747,#363636)}
.brand{position:absolute;left:70px;top:8px;display:flex;align-items:center;gap:8px}
.brand-mark{width:26px;height:26px;background:var(--crimson)}
.brand-name{color:var(--white);font-weight:600;font-size:10.5px;line-height:12px;text-transform:uppercase;letter-spacing:.3px}
.account{position:absolute;right:70px;top:12px;display:flex;align-items:center;gap:5px;font-size:8px;color:var(--white)}
.account a{display:inline-block;padding:3px 8px;font-size:7.5px;font-weight:700;text-decoration:none}
.btn-signup{background:var(--crimson);color:var(--white)}
.btn-login{background:var(--white);color:var(--crimson)}

.mainnav{top:44px;height:28px;background:var(--night);display:flex;justify-content:center}
.mainnav a{color:var(--white);font-size:9.5px;font-weight:600;text-decoration:none;padding:0 10px;line-height:28px}
.mainnav a.active{background:var(--crimson)}

.hero{top:72px;height:272px;background:radial-gradient(ellipse at 50% 75%,#6b5438 0%,#3e3226 40%,#1d1a17 80%)}
.hero-title{position:absolute;top:22px;width:100%;text-align:center;color:var(--white);font-weight:800;font-size:40px;line-height:45px;letter-spacing:1px}
.hero-title .hl{color:var(--yellow)}
.pillars{position:absolute;top:210px;left:0;width:100%;display:flex;justify-content:center;gap:60px}
.pillar{display:flex;align-items:center;gap:8px}
.pillar-bars{display:flex;flex-direction:column;gap:4px}
.pillar-bars span{display:block;width:92px;height:5px;background:var(--yellow)}
.pillar-label{color:var(--white);font-weight:700;font-size:10px;line-height:12px;text-transform:uppercase}

.focus{top:344px;height:136px;background:var(--graphite)}
.focus-icon{position:absolute;top:22px;width:72px;height:72px;border-radius:50%;border:4px solid var(--crimson);background:#2a2a2a;display:flex;align-items:center;justify-content:center}
.focus-icon.feature{top:14px;width:88px;height:88px;background:var(--white);border-color:var(--white);box-shadow:0 0 0 4px var(--graphite),0 0 0 6px var(--white)}
.focus-notch{position:absolute;left:344px;bottom:0;width:0;height:0;border-left:16px solid transparent;border-right:16px solid transparent;border-bottom:14px solid var(--paper)}

.welcome{top:480px;height:80px;background:var(--paper);text-align:center}
.welcome h1{font-weight:400;font-size:27px;color:var(--ink);margin-top:16px;letter-spacing:.3px}
.welcome p{font-size:14px;font-weight:600;color:var(--gold);text-transform:uppercase;letter-spacing:.5px;margin-top:2px}

.overview{top:560px;height:240px;background:var(--paper)}
.overview-photo{position:absolute;left:84px;top:0;width:348px;height:222px;border:5px solid var(--white);background:linear-gradient(160deg,#c9d7d8 0%,#8aa699 45%,#4f6f55 100%)}
.events{position:absolute;left:446px;top:2px;width:190px}
.events-head{display:flex;align-items:center;gap:6px;font-weight:700;font-size:13px;color:var(--crimson);text-transform:uppercase;border-bottom:2px solid var(--crimson);padding-bottom:6px}
.event{display:flex;gap:8px;padding:8px 0;border-bottom:1px solid #d6d6d6}
.event-thumb{width:40px;height:32px;flex:none;background:linear-gradient(#b7c4a8,#5d7350)}
.event-text{font-size:7.5px;line-height:10px;color:#555;text-transform:uppercase}
.event-text strong{color:var(--ink);font-weight:700}

.join{top:805px;height:54px;background:var(--graphite)}
.join h2{position:absolute;left:84px;top:12px;font-size:22px;font-weight:400;color:var(--white);text-transform:uppercase}
.join h2 b{color:var(--yellow);font-weight:700}
.join a{position:absolute;right:96px;top:15px;background:var(--crimson);color:var(--white);font-size:10px;font-weight:700;text-decoration:none;padding:6px 22px;text-transform:uppercase}

.newsletter{top:859px;height:91px;background:var(--crimson)}
.newsletter h3{position:absolute;left:84px;top:12px;font-weight:400;font-size:15px;color:var(--white)}
.newsletter h3 span{color:var(--yellow)}
.newsletter .field{position:absolute;top:46px;height:22px;background:var(--white);border:1px solid #ccc;font-size:8px;color:#999;padding:5px 7px}
.newsletter .subscribe{position:absolute;top:46px;left:484px;width:136px;height:22px;background:var(--navy);color:var(--white);font-size:9px;font-weight:700;text-align:center;line-height:22px;text-transform:uppercase}

.site-footer{top:950px;height:215px;background:var(--charcoal);color:var(--white)}
.col{position:absolute;top:18px}
.col h4{font-size:11px;font-weight:700;margin-bottom:12px;text-transform:capitalize}
.ad-list{list-style:none}
.ad-list li{font-size:7.5px;color:var(--muted);line-height:16px;padding-left:10px;position:relative}
.ad-list li::before{content:"";position:absolute;left:0;top:6px;width:4px;height:4px;background:var(--yellow)}
.form-field{width:178px;height:18px;background:var(--white);margin-bottom:6px;font-size:7px;color:#999;padding:4px 6px}
.form-field.tall{height:58px}
.form-submit{display:inline-block;background:var(--navy);color:var(--white);font-size:7.5px;font-weight:700;padding:4px 10px;text-transform:uppercase}
.social{list-style:none}
.social li{display:flex;align-items:center;gap:9px;font-size:11px;color:var(--yellow);line-height:26px}
.social li i{display:block;width:10px;height:10px;background:var(--yellow)}

.legal{top:1165px;height:35px;background:var(--navy);color:var(--white);font-size:9px;display:flex;align-items:center;gap:6px;padding-left:84px}
.legal i{width:8px;height:8px;border-radius:50%;border:1px solid var(--white);display:block}
</style>
</head>
<body>

<header class="topbar">
  <div class="brand">
    <span class="brand-mark"></span>
    <span class="brand-name">Lone Star Wetland<br>Flora Stewardship Guild</span>
  </div>
  <div class="account">
    <span>Become a member</span>
    <a class="btn-signup" href="#">SIGN UP</a>
    <a class="btn-login" href="#">LOGIN</a>
  </div>
</header>

<nav class="mainnav">
  <a href="#">HOME</a><a href="#">ABOUT US</a><a href="#">MEMBERS</a><a class="active" href="#">RESOURCES</a><a href="#">EVENTS</a><a href="#">MEMBERSHIP</a><a href="#">CONTACT</a>
</nav>

<section class="hero" role="img" aria-label="Photo of cupped hands holding soil with a young green seedling">
  <div class="hero-title">PROMOTING<br><span class="hl">ENVIRONMENTAL</span><br>STEWARDSHIP<br>THROUGH</div>
  <div class="pillars">
    <div class="pillar">
      <div class="pillar-bars"><span></span><span></span></div>
      <div class="pillar-label">Operations<br>Research</div>
    </div>
    <div class="pillar">
      <div class="pillar-bars"><span></span><span></span></div>
      <div class="pillar-label">Education and<br>Outreach</div>
    </div>
  </div>
</section>

<section class="focus">
  <div class="focus-icon" style="left:108px">
    <svg width="36" height="36" viewBox="0 0 36 36" fill="none" stroke="#f4d60c" stroke-width="3" stroke-linecap="round"><path d="M6 12 Q18 2 30 12"/><path d="M18 8 L18 32"/></svg>
  </div>
  <div class="focus-icon" style="left:216px">
    <svg width="36" height="36" viewBox="0 0 36 36"><circle cx="18" cy="14" r="9" fill="#f4d60c"/><rect x="14" y="23" width="8" height="7" fill="#f4d60c"/></svg>
  </div>
  <div class="focus-icon feature" style="left:316px">
    <svg width="44" height="44" viewBox="0 0 44 44" fill="none" stroke="#333" stroke-width="3" stroke-linecap="round"><path d="M22 40 L22 18"/><path d="M22 24 Q10 22 10 10 Q22 10 22 24"/><path d="M22 20 Q34 18 34 6 Q22 6 22 20"/></svg>
  </div>
  <div class="focus-icon" style="left:432px">
    <svg width="36" height="36" viewBox="0 0 36 36" fill="#f4d60c"><rect x="8" y="12" width="16" height="14" rx="2"/><path d="M24 15 L33 9 L33 13 L24 20 Z"/><rect x="4" y="28" width="26" height="3"/></svg>
  </div>
  <div class="focus-icon" style="left:540px">
    <svg width="36" height="36" viewBox="0 0 36 36" fill="none" stroke="#f4d60c" stroke-width="3"><circle cx="18" cy="18" r="12"/><path d="M6 18 H30 M18 6 Q11 18 18 30 M18 6 Q25 18 18 30"/></svg>
  </div>
  <div class="focus-notch"></div>
</section>

<section class="welcome">
  <h1>WELCOME TO LONE STAR WETLAND</h1>
  <p>Flora Stewardship Guild</p>
</section>

<section class="overview">
  <div class="overview-photo" role="img" aria-label="Photo of water lily pads floating on a calm pond"></div>
  <div class="events">
    <div class="events-head">
      <svg width="16" height="16" viewBox="0 0 16 16"><rect x="1" y="3" width="14" height="12" fill="#9a1d3f"/><rect x="3" y="7" width="10" height="6" fill="#fff"/><rect x="4" y="1" width="2" height="4" fill="#9a1d3f"/><rect x="10" y="1" width="2" height="4" fill="#9a1d3f"/></svg>
      Upcomming Events
    </div>
    <div class="event"><div class="event-thumb" role="img" aria-label="Event venue photo"></div><div class="event-text"><strong>2014 LSWFSG Conference</strong><br>January 22-24<br>Cedar Bend Ranch</div></div>
    <div class="event"><div class="event-thumb" role="img" aria-label="Event venue photo"></div><div class="event-text"><strong>2014 LSWFSG Conference</strong><br>December 18-20<br>Cedar Bend Ranch</div></div>
    <div class="event"><div class="event-thumb" role="img" aria-label="Event venue photo"></div><div class="event-text"><strong>2014 LSWFSG Conference</strong><br>October 12-14<br>Cedar Bend Ranch</div></div>
    <div class="event"><div class="event-thumb" role="img" aria-label="Event venue photo"></div><div class="event-text"><strong>2014 LSWFSG Conference</strong><br>October 12-14<br>Cedar Bend Ranch</div></div>
  </div>
</section>

<section class="join">
  <h2>Get LSWFSG <b>Membership</b></h2>
  <a href="#">Online Registration</a>
</section>

<section class="newsletter">
  <h3>Subscribe our <span>Newsletter.</span></h3>
  <div class="field" style="left:84px;width:196px">Name</div>
  <div class="field" style="left:292px;width:180px">Email</div>
  <div class="subscribe">Subscribe</div>
</section>

<footer class="site-footer">
  <div class="col" style="left:84px">
    <h4>Advertise With Us</h4>
    <ul class="ad-list">
      <li>Member ad placements</li>
      <li>Annual sponsor packages</li>
      <li>Event booth listings</li>
      <li>Newsletter banner slots</li>
      <li>Vendor directory entry</li>
      <li>Job board postings</li>
      <li>Field day sponsorship</li>
      <li>Custom ad requests</li>
    </ul>
  </div>
  <div class="col" style="left:276px">
    <h4>Quick Message</h4>
    <div class="form-field">Name</div>
    <div class="form-field">Email</div>
    <div class="form-field tall">Message</div>
    <span class="form-submit">Submit</span>
  </div>
  <div class="col" style="left:530px">
    <h4>Social Links</h4>
    <ul class="social">
      <li><i></i>Friendwall</li>
      <li><i></i>Chirpline</li>
      <li><i></i>Jobrungo</li>
    </ul>
  </div>
</footer>

<div class="legal" style="position:absolute;left:0;width:720px"><i></i>© LSWFSG 2014. All Right Reserved</div>

</body>
</html>
```